Acupuncture Medspa needs a business card design

I need a business card design that looks professional, has a spa-like quality and can offer a promo on the back. Initial promo is "First session free". The tagline of PinaVell is: Unwind, Mend, Glow.

PinaVell is a membership-based acupuncture medspa that offers acupuncture, cupping, and herbal therapies. Members choose between the "Refresh" membership which is for stress relief, or "Restore" which is for treating health conditions, and lastly "Rejuvenate" which is for natural facial enhancement.

Industry/Entity Type

Health And Wellness

Contact Information for Business Card

Doris Kettle, MAC, L.Ac.
614-385-2097
www.pinavell-example.com

Font styles to use
Serif
Sans Serif

Colors

Designer to choose colors to be used in the design.

Requirements
Must have
• The project must have PinaVell logo, promo on the back, and contact information
Nice to have
• I would like to see the colors of the logo used.

```html
<!DOCTYPE html>
<html lang="en">
<head>
<meta charset="utf-8">
<title>PinaVell Business Card</title>
<link rel="stylesheet" href="https://fonts.googleapis.com/css2?family=Montserrat:wght@600;700;800&family=Quicksand:wght@500;600;700&display=swap">
<style>
  :root {
    --teal: #128a85;
    --teal-deep: #0f7873;
    --cream: #fdf4d3;
    --icon-tint: #bfe0d6;
    --backdrop: #ecebe7;
  }
  * { box-sizing: border-box; margin: 0; padding: 0; }
  html, body { width: 1200px; height: 800px; overflow: hidden; }
  body {
    background: var(--backdrop);
    position: relative;
    font-family: "Quicksand", sans-serif;
    color: var(--teal);
  }
  .card {
    position: absolute;
    width: 530px;
    height: 303px;
    background: var(--cream);
    box-shadow: 0 10px 24px rgba(0,0,0,0.14);
    overflow: hidden;
  }
  .card--front { left: 80px; top: 90px; }
  .card--back { left: 590px; top: 405px; }

  /* Front */
  .brand {
    position: absolute;
    top: 70px; left: 0; right: 0;
    display: flex; align-items: center; justify-content: center; gap: 14px;
  }
  .brand__dot {
    width: 34px; height: 34px; border-radius: 50%;
    background: var(--teal);
  }
  .brand__name {
    font-family: "Montserrat", sans-serif;
    font-weight: 700;
    font-size: 46px;
    letter-spacing: 1px;
    color: var(--teal);
  }
  .tagline {
    position: absolute;
    top: 146px; left: 0; right: 0;
    text-align: center;
    font-family: "Montserrat", sans-serif;
    font-weight: 800;
    font-size: 13px;
    letter-spacing: 4.5px;
    text-transform: uppercase;
    color: var(--teal-deep);
  }
  .rule {
    position: absolute;
    top: 172px; left: 125px; right: 125px;
    height: 3px; background: var(--teal);
  }
  .contact {
    position: absolute;
    top: 192px; left: 0; right: 0;
    text-align: center;
    font-size: 12.5px;
    font-weight: 600;
    letter-spacing: 1.6px;
    line-height: 20px;
    color: var(--teal-deep);
  }

  /* Back */
  .packages {
    position: absolute;
    top: 62px; left: 40px; right: 40px;
    display: flex; justify-content: space-around;
  }
  .package {
    display: flex; flex-direction: column; align-items: center; gap: 14px;
  }
  .package__icon {
    width: 56px; height: 56px; border-radius: 8px;
    background: var(--icon-tint);
  }
  .package__label {
    font-weight: 700;
    font-size: 14px;
    letter-spacing: 3.5px;
    text-transform: uppercase;
    color: var(--teal);
  }
  .promo-band {
    position: absolute;
    left: 0; right: 0; bottom: 0;
    height: 92px;
    background: var(--teal);
    display: flex; align-items: center; justify-content: center;
  }
  .promo-band__text {
    font-weight: 700;
    font-size: 22px;
    letter-spacing: 6px;
    text-transform: uppercase;
    color: var(--cream);
  }
</style>
</head>
<body>
  <section class="card card--front" aria-label="Business card front">
    <div class="brand">
      <span class="brand__dot"></span>
      <span class="brand__name">PinaVell</span>
    </div>
    <p class="tagline">Unwind, Mend, Glow.</p>
    <div class="rule"></div>
    <div class="contact">
      <p>Doris Kettle, MAC, L.Ac.</p>
      <p>614-385-2097</p>
      <p>www.pinavell-example.com</p>
    </div>
  </section>

  <section class="card card--back" aria-label="Business card back">
    <div class="packages">
      <div class="package">
        <div class="package__icon" role="img" aria-label="Line icon of two lit candles"></div>
        <span class="package__label">Refresh</span>
      </div>
      <div class="package">
        <div class="package__icon" role="img" aria-label="Line icon of bamboo stalks with leaves"></div>
        <span class="package__label">Recover</span>
      </div>
      <div class="package">
        <div class="package__icon" role="img" aria-label="Line icon of a mortar and pestle"></div>
        <span class="package__label">Rejuvenate</span>
      </div>
    </div>
    <div class="promo-band">
      <span class="promo-band__text">First Session Free</span>
    </div>
  </section>
</body>
</html>
```